Fast Money - Simple Book Cover Design

Hello,

I am in need of a cover for my new book. The Book Title Is

"Standing Growth - Keys to Glowing Customer Ratings That Fill The Calendar and Draw Fresh Clients Through Every Entrance!"

Author: Fireman Dale Orsworth

What I want: This is a book for businesses on improving their online reputation. I want to have 5 Stars on the cover. You can look at this quarvex search for ideas of what I am meaning.....

(copy and paste)

http://www.quarvex-find.example/search?q=5+star+online+reviews&mode=images&ref=kx7Lp2QwZt9 (copy and paste)

I am open to different color schemes for the book. I am partial to dark blues if you make it look good. Here is another book that I really like the cover of....

http://www.brindlemart.example/Clipwave-Tactics-Earning-Promotion-ebook/item/Z93KT4WQPX

I want the cover BOLD and to STAND OUT.

I am looking for a design to help establish me as an authority for online reputation marketing. This book will be both in Pagely format and be used in print as well.

I am open to questions....

Thanks!

Dale

Reason: I don't believe we have received the right designs. I am going to give everyone more time...

Reason: Hi everyone, I had some stuff come up and was not able to be involved in this project. I am extending because we have not seen the exact thing we want and need time to work with designers to get it right. Thanks Dale

Reason: I am currently traveling and can't wrap this up until I get back.

Target Market(s)

Business Owners

Industry/Entity Type

Business

Requirements
Must have
• Title and Subtitle

Author Name

5 Stars Images....
Nice to have
• Creativity

Bold and stand out

Professional

Should not have
• thin text, small to read text, lame graphics,

```html
<!DOCTYPE html>
<html lang="en">
<head>
<meta charset="utf-8">
<title>Standing Growth – Book Cover</title>
<link rel="stylesheet" href="https://fonts.googleapis.com/css2?family=Black+Ops+One&family=Almendra+SC&display=swap">
<style>
  :root {
    --blue: #0b12e6;
    --blue-deep: #0a0fd0;
    --yellow: #fbff1e;
    --ink: #15162a;
    --highlight: rgba(255, 255, 255, 0.55);
    --shadow: rgba(0, 0, 0, 0.6);
    --plank: #5f6fd8;
    --star: #3a46b8;
  }
  * { margin: 0; padding: 0; box-sizing: border-box; }
  html, body { width: 1200px; height: 848px; overflow: hidden; }
  body { background: var(--blue); }

  .cover {
    position: relative;
    width: 1200px;
    height: 848px;
    overflow: hidden;
    background: linear-gradient(100deg,
      var(--blue-deep) 0%,
      #6a72a0 6%,
      var(--yellow) 17%,
      var(--yellow) 24%,
      #7c82a6 33%,
      var(--blue) 44%,
      var(--blue) 100%);
  }

  .cover-text {
    position: absolute;
    left: 48px;
    line-height: 1;
    color: var(--ink);
    white-space: nowrap;
    text-shadow: -1px -1px 0 var(--highlight), 3px 4px 5px var(--shadow);
  }

  .title {
    top: 4px;
    font-family: "Black Ops One", system-ui, sans-serif;
    font-size: 64px;
    letter-spacing: 4px;
    -webkit-text-stroke: 1.5px #9aa0c8;
  }

  .subtitle {
    top: 134px;
    font-family: "Almendra SC", serif;
    font-size: 56px;
  }

  .feature-lettering {
    position: absolute;
    left: 50px;
    top: 268px;
    width: 805px;
    height: 132px;
    background: linear-gradient(180deg, var(--plank), #3d4bc0);
    opacity: 0.75;
  }

  .stars {
    position: absolute;
    left: 0;
    top: 0;
    width: 1200px;
    height: 848px;
    pointer-events: none;
  }
  .star { fill: var(--star); stroke: #9aa4ee; stroke-width: 1.5; }

  .tagline {
    font-family: "Almendra SC", serif;
    font-size: 62px;
  }
  .tagline-1 { top: 451px; }
  .tagline-2 { top: 536px; }
  .tagline-3 { top: 622px; }

  .author {
    left: 285px;
    top: 784px;
    font-family: "Almendra SC", serif;
    font-size: 52px;
  }
</style>
</head>
<body>
  <main class="cover">
    <h1 class="cover-text title">STANDING GROWTH-</h1>
    <p class="cover-text subtitle">Keys to Glowing Customer Ratings</p>

    <div class="feature-lettering" role="img" aria-label="Hand-lettered word BUSINESS built from wooden planks in blue tones"></div>

    <svg class="stars" viewBox="0 0 1200 848" aria-hidden="true">
      <defs>
        <path id="four-point-star" d="M0,-26 L6,-6 L26,0 L6,6 L0,26 L-6,6 L-26,0 L-6,-6 Z"/>
      </defs>
      <use class="star" href="#four-point-star" x="85" y="254"/>
      <use class="star" href="#four-point-star" x="271" y="254"/>
      <use class="star" href="#four-point-star" x="570" y="254"/>
      <use class="star" href="#four-point-star" x="822" y="254"/>
      <use class="star" href="#four-point-star" x="1090" y="264"/>
    </svg>

    <p class="cover-text tagline tagline-1">That Fill The Calendar</p>
    <p class="cover-text tagline tagline-2">And Draw Fresh Clients</p>
    <p class="cover-text tagline tagline-3">Through Every Entrance!</p>

    <p class="cover-text author">by Fireman Dale Orsworth</p>
  </main>
</body>
</html>
```